Maple Grove Schools | brand new stationery!

We need stationery design with our new logo! Our company updated it's name and image and we like to incorporate the new one on our stationery, business cards and email signature. We are looking for fresh, new ideas!
Industry: Childcare, Elementary and Middle School
Company Name: Maple Grove Schools
Tagline: Bright Futures Start Here
Main colors: Blue, white and a little yellow
Star shape is something new for us! Do you see a way to incorporate it as a design element?

```html
<!DOCTYPE html>
<html lang="en">
<head>
<meta charset="utf-8">
<title>Maple Grove Schools – Business Card</title>
<link rel="stylesheet" href="https://fonts.googleapis.com/css2?family=Montserrat:wght@800&family=Poppins:wght@400;600&display=swap">
<style>
  :root {
    --backdrop: #c4c4c4;
    --card: #f2f2f2;
    --ink: #333333;
    --navy: #1b2b7e;
    --sun: #f2c12e;
  }
  * { margin: 0; padding: 0; box-sizing: border-box; }
  html, body { width: 1200px; height: 800px; overflow: hidden; }
  body {
    background: var(--backdrop);
    font-family: "Poppins", Arial, sans-serif;
    color: var(--ink);
    position: relative;
  }
  .card {
    position: absolute;
    top: 337px;
    width: 482px;
    height: 276px;
    background: var(--card);
    overflow: hidden;
  }
  .card--back { left: 97px; }
  .card--front { left: 612px; }

  .brand-mark {
    position: absolute;
    width: 250px;
    height: 250px;
    border-radius: 50%;
    background: var(--navy);
  }
  .card--back .brand-mark { left: 350px; top: 18px; }
  .card--front .brand-mark { left: -125px; top: 26px; }

  .wordmark {
    position: absolute;
    font-weight: 600;
    color: var(--ink);
    line-height: 1.05;
  }
  .card--back .wordmark { left: 42px; top: 22px; font-size: 33px; }
  .card--back .wordmark span { display: block; padding-left: 36px; }
  .card--front .wordmark { left: 170px; top: 96px; font-size: 42px; }
  .card--front .wordmark span { display: block; padding-left: 54px; }

  .person {
    position: absolute;
    left: 44px;
    top: 112px;
  }
  .person__name {
    font-family: "Montserrat", Arial, sans-serif;
    font-weight: 800;
    font-size: 22px;
    letter-spacing: -0.5px;
    color: var(--navy);
    line-height: 1.1;
  }
  .person__role { font-size: 13.5px; margin-top: 2px; }

  .contacts {
    position: absolute;
    left: 44px;
    top: 164px;
    list-style: none;
    font-size: 13.5px;
  }
  .contacts li {
    display: flex;
    align-items: center;
    gap: 9px;
    height: 19.5px;
  }
  .contacts svg { width: 12px; height: 12px; fill: var(--navy); }

  .address {
    position: absolute;
    left: 42px;
    top: 230px;
    font-size: 13.5px;
    font-style: normal;
    line-height: 1.35;
  }

  .tagline {
    position: absolute;
    left: 139px;
    top: 214px;
    font-size: 22px;
    color: var(--ink);
  }
</style>
</head>
<body>
  <section class="card card--back">
    <div class="brand-mark" aria-hidden="true"></div>
    <h1 class="wordmark">Maple Grove<span>Schools</span></h1>
    <div class="person">
      <p class="person__name">DANIEL HARPER</p>
      <p class="person__role">Managing Director</p>
    </div>
    <ul class="contacts">
      <li><svg viewBox="0 0 24 24"><path d="M6.6 10.8a15 15 0 0 0 6.6 6.6l2.2-2.2c.3-.3.7-.4 1-.2 1.1.4 2.3.6 3.6.6.6 0 1 .4 1 1V20c0 .6-.4 1-1 1A17 17 0 0 1 3 4c0-.6.4-1 1-1h3.5c.6 0 1 .4 1 1 0 1.3.2 2.5.6 3.6.1.3 0 .7-.2 1z"/></svg>044-987 654 321</li>
      <li><svg viewBox="0 0 24 24"><path d="M2 5h20v14H2zm2 2v.5l8 5 8-5V7l-8 5z"/></svg>hello@maplegrove.edu</li>
      <li><svg viewBox="0 0 24 24"><path d="M12 2a10 10 0 1 0 0 20 10 10 0 0 0 0-20zm6.9 6h-3a15 15 0 0 0-1.3-4 8 8 0 0 1 4.3 4zM12 4c.8 1.2 1.5 2.5 1.9 4h-3.8c.4-1.5 1.1-2.8 1.9-4zM4.3 14a8 8 0 0 1 0-4h3.4a16 16 0 0 0 0 4zm.8 2h3a15 15 0 0 0 1.3 4 8 8 0 0 1-4.3-4zm3-8h-3a8 8 0 0 1 4.3-4 15 15 0 0 0-1.3 4zM12 20c-.8-1.2-1.5-2.5-1.9-4h3.8c-.4 1.5-1.1 2.8-1.9 4zm2.3-6H9.7a14 14 0 0 1 0-4h4.6a14 14 0 0 1 0 4zm.3 5.6a15 15 0 0 0 1.3-3.6h3a8 8 0 0 1-4.3 3.6zM16.3 14a16 16 0 0 0 0-4h3.4a8 8 0 0 1 0 4z"/></svg>www.maplegrove.edu</li>
    </ul>
    <address class="address">18, Orchard Lane West<br>Brookfield, 45870</address>
  </section>

  <section class="card card--front">
    <div class="brand-mark" aria-hidden="true"></div>
    <h2 class="wordmark">Maple Grove<span>Schools</span></h2>
    <p class="tagline">Bright Futures Start Here</p>
  </section>
</body>
</html>
```